Stationary Set and Logo Update **PAYMENT GUARANTEED**

Stationery Design and Logo Update

About Us

Trindex Supply is a wholesale distributor of OEM [original brand] and compatible [generic brand] parts and supplies for use in copiers, faxes, printers, and multi-function machines. In plain English…we sell all the parts and supplies [such as toner] that make up any office equipment which outputs an image on paper.

Trindex was the 1st distributor to develop and sell a generic brand copier part in the United States. We have been in business since 1972 [nearly 40 years]. Our tagline is "The Steady Choice," as in our company was the first alternative product that copier dealers had to buying original brand copier parts. Trindex is known for offering reliable and cost-effective OEM and compatible products.

Project

We require a fresh, modern and corporate identity. Please submit a stationary package inclusive of a double-sided business card (2" x 3.5"), letterhead (8.5'x11"), and standard #10 envelope (4-1/8” x 9-1/2). You may use our current logo or preferably your take on an updated one. If an attempt is made in updating the logo #004D8E or a similar hue should be used as the primary color.

The design should be clean, simple, modern and professional and make an immediate impact.

Target Market(s)

Copier and printer dealers who lease and service imaging equipment in the United States and Latin America.

Industry/Entity Type

Business

Requirements
Must have
• Simple, clean, modern and professional. Please use #004D8E or a similar hue as the primary color. Letterhead must accommate (2) addresses. We have 2 locations.
Nice to have
• A simple, modern update to our current logo. https://assets.mailvorbo.example/fs030/5520384417702/img/418.jpg
Should not have
• More than (2) colors on logo.

```html
<!DOCTYPE html>
<html lang="en">
<head>
<meta charset="utf-8">
<title>Trindex Stationery Set</title>
<link href="https://fonts.googleapis.com/css2?family=Roboto:wght@400;700;900&display=swap" rel="stylesheet">
<style>
:root{
  --brand:#1f4f8f;
  --paper:#ffffff;
  --stage:#f7f7fc;
  --ink-light:#d6e0f0;
  --ink-muted:#6a7387;
  --shadow:rgba(20,30,60,.22);
}
*{margin:0;padding:0;box-sizing:border-box}
html,body{width:1200px;height:1200px;overflow:hidden;background:var(--stage);font-family:"Roboto",Arial,sans-serif}
.canvas{position:relative;width:1200px;height:1200px}
.sheet{position:absolute;background:var(--paper);box-shadow:2px 3px 8px var(--shadow)}

/* wordmark */
.logo{position:absolute;display:flex;align-items:center;gap:7px;color:var(--brand)}
.logo-dot{width:.6em;height:.6em;border-radius:50%;background:currentColor;flex:none}
.logo-name{font-weight:900;letter-spacing:-.01em;line-height:1}
.logo--large{font-size:40px}
.logo--white{color:var(--paper)}

/* letterhead */
.letterhead{left:44px;top:51px;width:849px;height:1098px}
.letterhead .logo{left:76px;top:72px}
.letterhead-footer{position:absolute;left:0;top:949px;width:100%;height:124px;background:var(--brand)}

/* address blocks */
.address{position:absolute;color:var(--ink-light);font-size:10px;line-height:12.6px;white-space:nowrap}
.address-title{color:var(--paper);font-weight:700}
.address-sub{color:var(--paper)}
.row{display:flex;white-space:nowrap}
.row .label{width:46px;flex:none}
.letterhead-footer .address.corporate{left:441px;top:15px}
.letterhead-footer .address.west{left:644px;top:15px}

/* envelope */
.envelope{left:204px;top:244px;width:951px;height:540px}
.envelope-flap{position:absolute;left:0;top:0;width:100%;height:127px;background:var(--brand);border-radius:18px 18px 0 0}
.return-address{position:absolute;right:74px;top:20px;transform:rotate(180deg);font-size:9px;line-height:11.5px;color:var(--ink-light);white-space:nowrap}
.return-address .address-title{color:var(--paper)}
.envelope .logo{left:76px;top:292px}

/* card back */
.card-back{left:603px;top:533px;width:349px;height:199px;background:var(--brand)}
.card-back .logo{left:26px;top:80px;font-size:34px}

/* card front */
.card-front{left:747px;top:761px;width:349px;height:199px}
.card-person{position:absolute;left:24px;top:24px}
.person-name{color:var(--brand);font-weight:700;font-size:12.5px;line-height:15px}
.person-role{color:var(--ink-muted);font-size:9px}
.card-band{position:absolute;left:0;top:62px;width:100%;height:120px;background:var(--brand)}
.card-band .address{font-size:9px;line-height:11.5px;top:17px}
.card-band .address.corporate{left:25px}
.card-band .address.west{left:194px}
.card-band .row .label{width:40px}
</style>
</head>
<body>
<main class="canvas">

  <section class="sheet letterhead" aria-label="Letterhead">
    <div class="logo logo--large"><span class="logo-dot"></span><span class="logo-name">Trindex</span></div>
    <footer class="letterhead-footer">
      <div class="address corporate">
        <div class="address-title">Trindex Supply</div>
        <div class="address-sub">Corporate Office</div>
        <div>2275 NW 18th Street</div>
        <div>Coral Springs, FL 33065</div>
        <div class="row"><span class="label">Toll Free</span>:&nbsp; 800.555.0140</div>
        <div class="row"><span class="label">Local</span>:&nbsp; 954.555.0127</div>
        <div class="row"><span class="label">Fax</span>:&nbsp; 954.555.0163</div>
      </div>
      <div class="address west">
        <div class="address-title">Trindex West</div>
        <div class="address-sub">West Coast Fulfillment Center</div>
        <div>Ridgeline Commerce Park #6</div>
        <div>940 Sandler Court</div>
        <div>Sparks, NV 89502</div>
        <div class="row"><span class="label">Toll Free</span>:&nbsp; 800.555.0171</div>
        <div class="row"><span class="label">Fax</span>:&nbsp; 775.555.0119</div>
      </div>
    </footer>
  </section>

  <section class="sheet envelope" aria-label="Number 10 envelope">
    <div class="envelope-flap">
      <div class="return-address">
        <div class="address-title">Trindex West</div>
        <div>West Coast Fulfillment Center</div>
        <div>Ridgeline Commerce Park #6</div>
        <div>940 Sandler Court</div>
        <div>Sparks, NV 89502</div>
      </div>
    </div>
    <div class="logo logo--large"><span class="logo-dot"></span><span class="logo-name">Trindex</span></div>
  </section>

  <section class="sheet card-back" aria-label="Business card back">
    <div class="logo logo--white"><span class="logo-dot"></span><span class="logo-name">Trindex</span></div>
  </section>

  <section class="sheet card-front" aria-label="Business card front">
    <div class="card-person">
      <div class="person-name">Marisol Venegas</div>
      <div class="person-role">Marketing Coordinator</div>
    </div>
    <div class="card-band">
      <div class="address corporate">
        <div class="address-title">Trindex Supply</div>
        <div class="address-sub">Corporate Office</div>
        <div>2275 NW 18th Street</div>
        <div>Coral Springs, FL 33065</div>
        <div class="row"><span class="label">Toll Free</span>:&nbsp; 800.555.0140</div>
        <div class="row"><span class="label">Direct</span>:&nbsp; 954.555.0182</div>
        <div class="row"><span class="label">Email</span>:&nbsp; mvenegas@trindex.example</div>
      </div>
      <div class="address west">
        <div class="address-title">Trindex West</div>
        <div class="address-sub">West Coast Fulfillment Center</div>
        <div>Ridgeline Commerce Park #6</div>
        <div>940 Sandler Court</div>
        <div>Sparks, NV 89502</div>
      </div>
    </div>
  </section>

</main>
</body>
</html>
```